New Business Card Design for Manufacturing

We are an engineering/manufacturing company that offers Advanced machining/assembly/engineering services, as well as innovative products for the heavy duty engine cooling markets.

We are looking to get a new business card designed that is clean and modern looking, but still fits the wide range of technical/skilled work we do.

- We hope to use this design as the base for other design work in new Presentations, web, and print work.

Industry/Entity Type

Engineering

Contact Information for Business Card

Our preferred color of blue is (RGB) 22/71/159 but can vary slightly from that color. Our content will be our Logo and full company name (Corvath Tooling Works, Inc.), company address, name, job title, phone number with extension, cell number, fax number, website, and email address on the cards.
We'd like the full company name next to the logo, but we are open to other interpretations of that layout.
Preferably, we would like the back side to be clean with just our logo, and the front to contain all of the contact information.

Colors
2f74b4
0355a3
85abd2

Requirements
Must have
• - Logo, company name, needed content - We are open to interpretation beyond that.
• - Standard size business card.
• - Horizontal orientation.
• - Enough space for lengthy names / job titles (for example, a job title could read "Directory of Human Resources" or "V.P. of Governmental Affairs"). We need this to look clean, whether the title be short (CEO) or long (as described above).

```html
<!DOCTYPE html>
<html lang="en">
<head>
<meta charset="utf-8">
<title>Corvath Tooling Works — Business Card</title>
<link rel="stylesheet" href="https://fonts.googleapis.com/css2?family=Source+Sans+3:wght@400;600;700&display=swap">
<style>
  :root {
    --brand-blue: #16479f;
    --card-blue: #1b58b4;
    --deep-blue: #0f3f8c;
    --paper: #f4f6f8;
    --ink-grey: #4a4d52;
    --rule-grey: #a9adb3;
    --band-grey: #9a9ea4;
    --stage: #e4e6ea;
  }
  * { box-sizing: border-box; margin: 0; padding: 0; }
  html, body {
    width: 1200px; height: 862px; overflow: hidden;
    background: var(--stage);
    font-family: "Source Sans 3", Arial, sans-serif;
  }
  .stage {
    width: 1200px; height: 862px;
    display: flex; flex-direction: column;
    align-items: center; justify-content: center; gap: 46px;
  }
  .card {
    position: relative;
    width: 630px; height: 360px;
    overflow: hidden;
    box-shadow: 0 6px 18px rgba(0,0,0,.18);
  }

  /* Back side */
  .card-back { background: var(--card-blue); }
  .card-back .wordmark {
    position: absolute; left: 0; right: 0; top: 128px;
    text-align: center;
    font-size: 40px; font-weight: 700; color: var(--deep-blue);
    letter-spacing: .5px;
  }
  .card-back .back-email {
    position: absolute; left: 0; right: 0; top: 186px;
    text-align: center; font-size: 14px; color: var(--deep-blue);
    letter-spacing: 1px;
  }
  .card-back .back-web {
    position: absolute; left: 0; right: 0; bottom: 54px;
    text-align: center; font-size: 14px; color: var(--deep-blue);
    letter-spacing: 1px;
  }

  /* Front side */
  .card-front { background: var(--paper); }
  .brand {
    position: absolute; left: 40px; top: 66px;
    display: flex; align-items: center; gap: 12px;
  }
  .brand-mark { width: 26px; height: 26px; background: var(--brand-blue); }
  .brand-name {
    font-size: 27px; font-weight: 700; color: var(--brand-blue);
    line-height: 1;
  }
  .person {
    position: absolute; right: 40px; top: 62px; width: 270px;
    text-align: right;
    border-bottom: 1px solid var(--rule-grey);
    padding-bottom: 8px;
  }
  .person-name {
    font-size: 22px; font-weight: 700; color: var(--brand-blue);
    letter-spacing: .5px;
  }
  .person-title { font-size: 13px; color: var(--ink-grey); margin-top: 2px; }

  .address {
    position: absolute; right: 40px; top: 150px;
    text-align: right; font-size: 13.5px; line-height: 1.55;
    color: var(--ink-grey);
  }
  .label { color: var(--brand-blue); }

  .contacts {
    position: absolute; left: 40px; top: 208px; width: 270px;
    border-top: 1px solid var(--rule-grey);
    padding-top: 12px;
    font-size: 14px; line-height: 1.6; color: var(--ink-grey);
    list-style: none;
  }
  .edge-band { position: absolute; left: 0; bottom: 0; width: 630px; height: 10px; }
</style>
</head>
<body>
<main class="stage">

  <section class="card card-back" aria-label="Business card back">
    <div class="wordmark">Corvath Tooling Works</div>
    <div class="back-email">www.corvathtooling.com</div>
    <div class="back-web">www.corvathtooling.com</div>
  </section>

  <section class="card card-front" aria-label="Business card front">
    <div class="brand">
      <span class="brand-mark"></span>
      <span class="brand-name">Corvath Tooling Works</span>
    </div>

    <div class="person">
      <div class="person-name">DARA L. K. WHITFIELD</div>
      <div class="person-title">President</div>
    </div>

    <address class="address" style="font-style:normal">
      <div><span class="label">Address:</span> Street Name Avenue, Suite</div>
      <div>100 State, Zip Code, Country</div>
      <div><span class="label">Web:</span> www.corvathtooling.com</div>
    </address>

    <ul class="contacts">
      <li><span class="label">Office:</span> +000.000.00 00</li>
      <li><span class="label">Cell:</span> +000.000.00 00</li>
      <li><span class="label">Fax:</span> +000.000.00 00</li>
      <li><span class="label">Email:</span> www.corvathtooling.com</li>
    </ul>

    <svg class="edge-band" viewBox="0 0 630 10" preserveAspectRatio="none" aria-hidden="true">
      <polygon points="0,0 400,0 392,10 0,10" fill="var(--brand-blue)"/>
      <polygon points="406,0 630,0 630,10 398,10" fill="var(--band-grey)"/>
    </svg>
  </section>

</main>
</body>
</html>
```